Mental Health & Addiction Podcast Art

Project: Podcast Cover Art / Visual Identity
Podcast Name: The Renewal Compass
Focus: Recovery from substance use and mental health
Objectives
Create compelling podcast artwork that:
Reflects the themes of hope, healing, and personal growth
Establishes credibility and professionalism
Appeals to individuals seeking recovery resources and support
Maintains strong brand consistency with Harborline Wellness
Brand Integration Requirements
Logo incorporation: Integrate an element from the Harborline Wellness Logo—potentially an abstract or partial use of the sun motif
Flexibility: Open to creative interpretations (e.g., sun rays as background texture, sunrise gradient, partial sun as a design accent)
Mandatory: Must adhere to existing Harborline Wellness brand guidelines (approved color palette, typography, and visual style)

Target Market(s)

United states, people with addiction and mental health disorders.

Industry/Entity Type

Wellness

Font styles to use
Other font styles liked:
• See Brand Guide

Requirements
Must have
• Match brand guide, in corporate elements of the Harborline Wellness Logo icon

```html
<!DOCTYPE html>
<html lang="en">
<head>
<meta charset="utf-8">
<title>The Renewal Compass — Podcast Cover</title>
<link rel="stylesheet" href="https://fonts.googleapis.com/css2?family=Alegreya+Sans:wght@400;800&display=swap">
<style>
  :root {
    --page: #e9e6e1;
    --cream: #f5e9cd;
    --sand: #f1d9a4;
    --gold: #efbd62;
    --peach: #e6a06a;
    --ember: #e07a4a;
    --sea: #2d5479;
    --navy: #1e2a3e;
    --ink: #1f2b40;
    --light: #f3ead9;
  }
  * { margin: 0; padding: 0; box-sizing: border-box; }
  html, body {
    width: 1200px; height: 911px; overflow: hidden;
    background: var(--page);
  }
  .canvas { position: relative; width: 1200px; height: 911px; }
  .cover {
    position: absolute; left: 170px; top: 25px;
    width: 860px; height: 860px; overflow: hidden;
    background: var(--cream);
    box-shadow: 0 10px 30px rgba(30, 42, 62, 0.18);
  }
  .cover__art {
    position: absolute; inset: 0;
    background: linear-gradient(180deg,
      var(--cream) 0%,
      var(--sand) 38%,
      var(--gold) 54%,
      var(--peach) 63%,
      var(--ember) 68%,
      var(--sea) 75%,
      var(--navy) 84%,
      var(--navy) 100%);
  }
  .cover__title {
    position: absolute; left: 0; right: 0; top: 100px;
    text-align: center; color: var(--ink);
    font-family: "Alegreya Sans", sans-serif; text-transform: uppercase;
  }
  .cover__kicker {
    display: block; font-weight: 400; font-size: 92px; line-height: 0.95; letter-spacing: 1px;
  }
  .cover__name {
    display: block; font-weight: 800; font-size: 104px; line-height: 0.98; letter-spacing: 1px;
  }
  .brand {
    position: absolute; left: 0; right: 0; top: 672px;
    display: flex; flex-direction: column; align-items: center; gap: 14px;
  }
  .brand__mark {
    width: 56px; height: 56px; border-radius: 50%;
    border: 3px solid var(--light);
  }
  .brand__name {
    font-family: "Alegreya Sans", sans-serif; font-weight: 400;
    font-size: 36px; line-height: 1.05; letter-spacing: 2px;
    text-transform: uppercase; color: var(--light); text-align: center;
  }
</style>
</head>
<body>
<main class="canvas">
  <section class="cover">
    <div class="cover__art" role="img" aria-label="Illustration of a sun rising with rays over layered golden hills and deep blue waves"></div>

    <h1 class="cover__title">
      <span class="cover__kicker">The</span>
      <span class="cover__name">Renewal<br>Compass</span>
    </h1>

    <div class="brand">
      <span class="brand__mark"></span>
      <span class="brand__name">Harborline<br>Wellness</span>
    </div>
  </section>
</main>
</body>
</html>
```